Business card design needed to incorporate existing logo

We need a business card for a new modern Accounting & Business Solutions company call KelvaTrade Services.com.au servicing all of Australia.
My tagline is Steady Ledger Answers... built right.

We specialise in Cloud Accounting and this is our primary focus. We also provide tax representation, debt recovery, computer, tablet and smart phone sales.

I would like a design that uses my corporate, trustworthy colours of blue/white, black/grey however am open to suggestion. I have attached my logo to go on the card somewhere,of which you will see the colour scheme.

I am after a card that STANDS OUT, somewhere between it not being too busy and not being a baron waste of space.

A 'cloud' incorporated in the design may work well, up to your artistic judgement. I know what I like when I see it; it is harder to put into words!

Excited to see your ideas!
I have added my logo predominately (blue/white) and for additional opportunity have added my reverse logo (darker one). I have used the blue/white on my website and letterhead. I will be using both on my vehicle signage.

Target Market(s)

Tradesmen and small-medium businesses of all descriptions Australia-wide

Industry/Entity Type

Debt

Contact Information for Business Card

Dale Pemberton
Principal (optional)
KelvaTrade Services.com.au
Steady Ledger Answers... built right

P: 1800 513 684
M: 0412 860 571 (optional)
W: www.kelvatradeservices.com.au
E: admin@kelvatradeservices.com.au

Logo Text

Steady Ledger Answers... built right!

Logo styles of interest
Wordmark Logo
Requirements
Must have
• Must look professional and of high quality not cheap.

My logo and my tagline 'Steady Ledger Answers... built right'.

I have my colourscheme in mind as per my attached logo, however am open to suggestion. I want to see what you can create that I would not have thought of.

Modern, innovative.
Something I won't look at and think, 'I could have done that myself'.

Must be able to be printed on Norla 300gm premium cards and the artwork provided to me.
Nice to have
• Title of Principal is optional depending on space and judement call of look/fee.
M: (mobile) number is also optional as above.

Somthing cloud related given the Cloud Accounting aspect may be relevant. I leave it to your artistic design and judgement.
Should not have
• Must not look cheap.

```html
<!DOCTYPE html>
<html lang="en">
<head>
<meta charset="utf-8">
<title>KelvaTrade Services – Business Card</title>
<link href="https://fonts.googleapis.com/css2?family=Arimo:wght@400;700&display=swap" rel="stylesheet">
<style>
  :root {
    --page-bg: #dcdde0;
    --card-white: #f4f4f5;
    --card-grey: #d9dadc;
    --navy: #0b1670;
    --navy-deep: #07104f;
    --royal: #1f31a8;
    --sky: #4a9be6;
    --sky-light: #7fc0f2;
    --ink: #141414;
    --white: #ffffff;
  }
  * { margin: 0; padding: 0; box-sizing: border-box; }
  html, body {
    width: 960px; height: 1200px; overflow: hidden;
    background: var(--page-bg);
    font-family: "Arimo", Arial, sans-serif;
  }
  .canvas { position: relative; width: 960px; height: 1200px; }

  .card {
    position: absolute; left: 30px; width: 900px; height: 510px;
    overflow: hidden;
    box-shadow: 0 6px 18px rgba(0,0,0,0.25);
  }

  /* Front */
  .card-front {
    top: 40px;
    background: radial-gradient(ellipse at 50% 40%, var(--card-white) 0%, var(--card-white) 45%, var(--card-grey) 100%);
  }
  .front-band {
    position: absolute; left: 0; top: 153px; width: 100%; height: 153px;
    background: var(--navy);
    box-shadow: 0 3px 8px rgba(0,0,0,0.35), 0 -3px 8px rgba(0,0,0,0.2);
    display: flex; align-items: center; justify-content: center; gap: 16px;
  }
  .brand-dot {
    width: 30px; height: 30px; border-radius: 50%;
    background: var(--sky);
  }
  .brand-name {
    color: var(--white); font-weight: 400; font-size: 38px; letter-spacing: 1px;
  }

  /* Back */
  .card-back { top: 630px; display: flex; }
  .back-brand-panel {
    position: relative; width: 450px; height: 100%;
    background: linear-gradient(90deg, var(--royal) 0%, var(--navy) 60%, var(--navy-deep) 100%);
  }
  .brand-disc {
    position: absolute; left: 117px; top: 93px; width: 200px; height: 200px;
    border-radius: 50%; background: var(--sky);
  }
  .panel-name {
    position: absolute; left: 59px; top: 297px;
    color: var(--sky); font-size: 26px; font-weight: 400;
  }
  .panel-tagline {
    position: absolute; left: 59px; top: 350px;
    color: var(--white); font-size: 17px; font-weight: 400;
  }
  .back-contact-panel {
    position: relative; width: 450px; height: 100%;
    background: radial-gradient(ellipse at 60% 40%, var(--card-white) 0%, var(--card-grey) 100%);
  }
  .person {
    position: absolute; right: 39px; top: 56px; text-align: left;
  }
  .person-name { color: var(--navy); font-weight: 700; font-size: 30px; }
  .person-title { color: var(--ink); font-size: 18px; margin-top: 4px; }
  .contact-list {
    position: absolute; left: 21px; top: 352px;
    list-style: none; color: var(--ink); font-size: 18px; line-height: 25px;
  }
  .contact-label { font-weight: 700; color: var(--navy); display: inline-block; width: 30px; }
</style>
</head>
<body>
<div class="canvas">
  <section class="card card-front">
    <div class="front-band">
      <span class="brand-dot"></span>
      <span class="brand-name">KelvaTrade Services.com.au</span>
    </div>
  </section>

  <section class="card card-back">
    <div class="back-brand-panel">
      <div class="brand-disc"></div>
      <p class="panel-name">KelvaTradeServices.com.au</p>
      <p class="panel-tagline">Steady Ledger Answers... built right</p>
    </div>
    <div class="back-contact-panel">
      <div class="person">
        <p class="person-name">Dale Pemberton</p>
        <p class="person-title">Principal</p>
      </div>
      <ul class="contact-list">
        <li><span class="contact-label">P :</span>1800 513 684</li>
        <li><span class="contact-label">M:</span>0412 860 571</li>
        <li><span class="contact-label">E :</span>admin@kelvatradeservices.com.au</li>
      </ul>
    </div>
  </section>
</div>
</body>
</html>
```